Local massage therapist needs some new marketing material

Hi there! I am a massage therapist here in Denver, CO in Brindle Hollow(shopping and art district) of the city. My business is called Lunora Massage Studio. My practice has an eastern influence and I do reflexology, thai massage and use Chinese herbs, etc. I know all my clients and pay close attention to details. I am also very respectful of tradition and it shows in how I work. I tend to like modern, clean, fun, Asian designs. I am wanting a new business card and brochure. I have a logo and branding for my business that I want used in the design. Currently, the sign for my building is purple and I think my logo was designed to be purple. I will attach pictures of it and can send whatever files are necessary so it can be integrated into the brochure, etc. I like the purple but open to using other colors as well. Thanks!
My website is lunoramassagestudio.example where info can be gathered about me and services/fees for brochure.
Updates

Just increased budget. Please see new feedback in discussion thread.

Thanks!

                                       HEY ALL,

Just wanted to let you know that I made a change to my website. It is on the Prices Page. I no longer have the frequent  flyer prices but I added discounts. Let me know if you have any questions. Thanks so much!

Target Market(s)

healthy, urban, educated, upper middle class, yogis

Industry/Entity Type

Marketing

Requirements
Must have
• logo stays purple
Should not have
• not too busy

```html
<!DOCTYPE html>
<html lang="en">
<head>
<meta charset="utf-8">
<title>Lunora Massage Studio – Business Card</title>
<link rel="stylesheet" href="https://fonts.googleapis.com/css2?family=Open+Sans:ital,wght@0,300;0,400;0,600;0,700;1,400&display=swap">
<style>
  :root {
    --purple: #662d91;
    --ink: #3a3a3a;
    --grey: #6b6b6b;
    --rule: #9a9a9a;
    --dark-band: #2f2f2f;
    --paper: #ffffff;
    --backdrop: #e9e9ee;
  }
  * { box-sizing: border-box; margin: 0; padding: 0; }
  html, body { width: 1200px; height: 987px; overflow: hidden; }
  body {
    background: var(--backdrop);
    font-family: "Open Sans", Arial, sans-serif;
    color: var(--ink);
    position: relative;
  }
  .card {
    position: absolute;
    left: 220px;
    width: 760px;
    height: 434px;
    background: var(--paper);
    border-radius: 22px;
    overflow: hidden;
    box-shadow: 0 6px 18px rgba(0,0,0,0.12);
  }
  .card--front { top: 40px; }
  .card--back { top: 513px; }

  /* Front */
  .wordmark {
    position: absolute;
    color: var(--purple);
    font-weight: 400;
    letter-spacing: 6px;
    line-height: 1;
    white-space: nowrap;
  }
  .card--front .wordmark { left: 40px; top: 150px; font-size: 64px; }
  .divider {
    position: absolute;
    left: 365px; top: 100px;
    width: 2px; height: 200px;
    background: var(--rule);
  }
  .contact {
    position: absolute;
    left: 390px; top: 104px;
    width: 350px;
  }
  .contact__name { color: var(--purple); font-weight: 700; font-size: 34px; line-height: 1.1; }
  .contact__title { color: var(--grey); font-size: 20px; margin-bottom: 16px; }
  .contact__row { display: flex; align-items: center; gap: 8px; font-size: 20px; color: var(--ink); margin-bottom: 8px; white-space: nowrap; }
  .contact__row--email { font-size: 17px; }
  .contact__row--address { font-size: 18px; }
  .contact__row svg { flex: none; }
  .bands { position: absolute; left: 0; bottom: 0; }
  .website {
    position: absolute;
    left: 36px; bottom: 20px;
    color: var(--paper);
    font-size: 22px;
    letter-spacing: 3px;
  }

  /* Back */
  .appointment { position: absolute; left: 50px; top: 46px; width: 660px; }
  .appointment__heading { color: var(--purple); font-weight: 700; font-size: 20px; letter-spacing: 0.5px; margin-bottom: 22px; }
  .field-row { display: flex; align-items: flex-end; gap: 10px; font-size: 20px; color: var(--ink); margin-bottom: 18px; }
  .field-line { flex: 1; border-bottom: 1px dotted var(--rule); height: 18px; }
  .field-line--short { flex: 0 0 170px; }
  .hours { font-size: 21px; line-height: 1.4; margin-top: 10px; color: var(--ink); }
  .notice { font-style: italic; font-size: 19px; color: var(--grey); margin-top: 8px; }
  .card--back .wordmark { right: 44px; bottom: 40px; font-size: 58px; letter-spacing: 5px; }
</style>
</head>
<body>

<section class="card card--front" aria-label="Business card front">
  <div class="wordmark">LUNORA</div>
  <div class="divider"></div>
  <div class="contact">
    <p class="contact__name">Your Name</p>
    <p class="contact__title">Title</p>
    <p class="contact__row">
      <svg width="20" height="20" viewBox="0 0 20 20" aria-hidden="true"><circle cx="10" cy="10" r="9" fill="var(--ink)"/><path d="M7 5.5l2 2-1.2 1.3c.6 1.3 1.5 2.2 2.8 2.8L11.9 10.4l2 2-1.3 1.6c-3.3-.3-6.3-3.3-6.6-6.6z" fill="#fff"/></svg>
      303.555.0148
    </p>
    <p class="contact__row contact__row--email">
      <svg width="20" height="20" viewBox="0 0 20 20" aria-hidden="true"><rect x="1" y="4" width="18" height="12" rx="2" fill="var(--ink)"/><path d="M2 5l8 6 8-6" stroke="#fff" stroke-width="1.5" fill="none"/></svg>
      info@lunoramassagestudio.example
    </p>
    <p class="contact__row contact__row--address">1480 E Alder Ave, Larkhaven, CO 80990</p>
  </div>
  <svg class="bands" width="760" height="130" viewBox="0 0 760 130" aria-hidden="true">
    <polygon points="0,24 320,24 300,56 0,56" fill="var(--dark-band)"/>
    <polygon points="0,64 300,64 320,52 620,52 580,130 0,130" fill="var(--purple)"/>
  </svg>
  <p class="website">www.lunoramassagestudio.example</p>
</section>

<section class="card card--back" aria-label="Business card back">
  <div class="appointment">
    <p class="appointment__heading">YOUR APPOINTMENT</p>
    <div class="field-row"><span>Name :</span><span class="field-line"></span></div>
    <div class="field-row"><span>Date :</span><span class="field-line field-line--short"></span><span>Time :</span><span class="field-line"></span><span>am / pm</span></div>
    <p class="hours">Wed - Sat 9am - 7pm Sun 11am-4pm<br>(Appointments required) No walk-ins please.</p>
    <p class="notice">We appreciate a 24 hr. notice for cancellations</p>
  </div>
  <div class="wordmark">LUNORA</div>
</section>

</body>
</html>
```